Brisk Meadow Builders needs a product brochure

We need a new flyer for our Patio Perch Lounge. Here is some of the copy your will need.
"Turn your back yard into the ultimate entertianment venue with the stunning Patio Perch Lounge!"
"Entertain family & friends in your very own back yard!"
"Available with or without solar and comes in a variety of colors"
"The Patio Perch Lounge measures 5' deep by 10' wide and is 9'-6" at it's highest point"
"Constructed with treated 4x4's, primed then painted with Thornby Calder best exterior paint for years of care free enjoyment. Also, Marlow Pendt Keystead shingles are dimensional, have a 25 year warranty and are rated for 150 mph winds!"
"TV Mount included. Shelves and TV are sold separately"
There also needs to be a box where we can add the price into later. The price can change from time to time due to material cost fluctuation.
Look and feel
Each slider illustrates characteristics of the customer's brand and the style your logo design should communicate.

```html
<!DOCTYPE html>
<html lang="en">
<head>
<meta charset="utf-8">
<title>Patio Perch Lounge – Brisk Meadow Builders</title>
<link href="https://fonts.googleapis.com/css2?family=Barlow+Semi+Condensed:wght@500;600&family=Poppins:wght@400;500;700&display=swap" rel="stylesheet">
<style>
  :root{
    --page:#e6e7e9;
    --paper:#ffffff;
    --green:#3f8f2e;
    --green-light:#6ab245;
    --yellow:#e9b934;
    --teal:#1f6f86;
    --navy:#222c41;
    --navy-deep:#131a29;
    --ink:#1d1d1d;
    --white:#ffffff;
  }
  *{box-sizing:border-box;margin:0;padding:0}
  html,body{width:1200px;height:1000px;overflow:hidden;background:var(--page)}
  .flyer{position:absolute;left:260px;top:20px;width:680px;height:960px;background:var(--paper);overflow:hidden;box-shadow:0 6px 20px rgba(0,0,0,.18)}

  .brand{position:absolute;display:flex;align-items:center;gap:7px;font-family:"Poppins",sans-serif;font-weight:700;color:var(--yellow);line-height:1.05}
  .brand-dot{width:12px;height:12px;border-radius:50%;background:var(--green-light);flex:none}
  .brand--header{left:46px;top:48px;font-size:19px}
  .brand--footer{left:42px;top:846px;font-size:19px}

  .phone{position:absolute;right:34px;top:30px;display:flex;align-items:center;gap:10px;font-family:"Poppins",sans-serif;font-weight:700;font-size:14px;color:var(--ink)}
  .icon-disc{width:28px;height:28px;border-radius:50%;background:var(--green);display:flex;align-items:center;justify-content:center}

  .photo-hero{position:absolute;inset:0;background:linear-gradient(160deg,#6f9a3c 0%,#4b4a42 45%,#8a6a3f 60%,#7c7f84 100%);clip-path:polygon(300px 130px,680px 68px,680px 508px,240px 508px)}
  .panel-green{position:absolute;inset:0;background:linear-gradient(180deg,#3f8f2e,#2f7a25);clip-path:polygon(0 125px,310px 125px,215px 404px,0 404px)}
  .panel-yellow{position:absolute;inset:0;background:var(--yellow);clip-path:polygon(0 404px,290px 404px,245px 508px,0 508px)}

  .headline{position:absolute;left:31px;top:164px;width:182px;font-family:"Poppins",sans-serif;font-weight:700;font-size:20.5px;line-height:27.4px;color:var(--white)}
  .spec{position:absolute;left:31px;top:420px;width:222px;font-family:"Barlow Semi Condensed",sans-serif;font-weight:500;font-size:16.5px;line-height:22px;color:var(--white)}

  .price-box{position:absolute;left:520px;top:430px;width:140px;height:62px;background:var(--navy-deep);border:2px solid var(--yellow);display:flex;flex-direction:column;justify-content:center;padding:0 12px;font-family:"Poppins",sans-serif;color:var(--white)}
  .price-label{font-size:11px;font-weight:500;letter-spacing:.08em;text-transform:uppercase;color:var(--yellow)}
  .price-value{font-size:20px;font-weight:700;line-height:1.2}

  .strip{position:absolute;left:0;top:508px;width:680px;height:147px;background:var(--yellow)}
  .thumb{position:absolute;top:521px;width:194px;height:121px}
  .thumb--1{left:30px;background:linear-gradient(135deg,#6b4a2c,#8f8b84 60%,#556b3a)}
  .thumb--2{left:243px;background:linear-gradient(135deg,#3a3b3e,#8d6a44 50%,#9aa0a6)}
  .thumb--3{left:456px;background:linear-gradient(135deg,#7a5432,#2a2d33 45%,#9a7048)}

  .note{position:absolute;left:50px;top:687px;font-family:"Barlow Semi Condensed",sans-serif;font-weight:600;font-size:22px;line-height:29px;color:var(--teal)}

  .dark-band{position:absolute;inset:0;background:linear-gradient(180deg,var(--navy),var(--navy-deep));clip-path:polygon(0 766px,318px 766px,402px 683px,680px 683px,680px 960px,0 960px)}
  .photo-frame{position:absolute;inset:0;background:var(--white);clip-path:polygon(392px 766px,450px 686px,672px 686px,614px 766px)}
  .photo-crowd{position:absolute;inset:0;background:linear-gradient(120deg,#6b4b2e,#b5314a 35%,#3b6a9a 60%,#8a6a44);clip-path:polygon(402px 760px,454px 691px,661px 691px,608px 760px)}

  .tagline{position:absolute;left:42px;top:782px;font-family:"Barlow Semi Condensed",sans-serif;font-weight:600;font-size:16px;line-height:20px;color:var(--green-light)}

  .details{position:absolute;left:234px;top:818px;width:248px;font-family:"Poppins",sans-serif;font-size:11px;line-height:13.5px;color:var(--white)}

  .badge{position:absolute;left:512px;top:784px;width:148px;height:148px}
  .badge-text{position:absolute;left:512px;top:820px;width:148px;text-align:center;font-family:"Poppins",sans-serif;font-size:13.5px;line-height:19px;color:var(--white)}

  .contact-bar{position:absolute;inset:0;background:var(--green-light);clip-path:polygon(158px 960px,192px 913px,572px 913px,538px 960px)}
  .contacts{position:absolute;left:206px;top:925px;display:flex;gap:16px;font-family:"Poppins",sans-serif;font-size:12.5px;color:var(--white)}
  .contact{display:flex;align-items:center;gap:8px}
  .contact .icon-disc{width:20px;height:20px;background:var(--navy-deep)}
</style>
</head>
<body>
  <main class="flyer">
    <div class="brand brand--header"><span class="brand-dot"></span>Brisk Meadow<br>Builders</div>
    <div class="phone">
      <span class="icon-disc"><svg width="14" height="14" viewBox="0 0 24 24"><path fill="#fff" d="M6.6 10.8a15.1 15.1 0 0 0 6.6 6.6l2.2-2.2c.3-.3.7-.4 1-.2 1.1.4 2.3.6 3.6.6.6 0 1 .4 1 1V20c0 .6-.4 1-1 1A17 17 0 0 1 3 4c0-.6.4-1 1-1h3.5c.6 0 1 .4 1 1 0 1.3.2 2.5.6 3.6.1.3 0 .7-.2 1z"/></svg></span>
      +1 555 214 7730
    </div>

    <div class="photo-hero" role="img" aria-label="Photo of the Patio Perch Lounge bar with solar panel roof, TV, shelves and three stools on a patio"></div>
    <div class="panel-green"></div>
    <div class="panel-yellow"></div>

    <h1 class="headline">Turn your back yard into the ultimate entertainment venue with the stunning Patio Perch Lounge!</h1>
    <p class="spec">The Patio Perch Lounge measures 5' deep by 10' wide and is 9'-6" at it's highest point</p>

    <div class="price-box">
      <span class="price-label">Price</span>
      <span class="price-value">$ ______</span>
    </div>

    <div class="strip"></div>
    <div class="thumb thumb--1" role="img" aria-label="Photo of guests enjoying drinks at the bar"></div>
    <div class="thumb thumb--2" role="img" aria-label="Photo of friends seated at the bar watching the game"></div>
    <div class="thumb thumb--3" role="img" aria-label="Photo of the bottle shelf and glass rack"></div>

    <p class="note">TV Mount included. Shelves<br>and TV are sold separately</p>

    <div class="dark-band"></div>
    <div class="photo-frame"></div>
    <div class="photo-crowd" role="img" aria-label="Photo of friends gathered at the bar with the TV on"></div>

    <p class="tagline">Entertain family &amp; friends in your very own back yard!</p>

    <div class="brand brand--footer"><span class="brand-dot"></span>Brisk Meadow<br>Builders</div>

    <p class="details">Constructed with treated 4x4's, primed then painted with Thornby Calder best exterior paint for years of care free enjoyment. Also, Marlow Pendt Keystead shingles are dimensional, have a 25 year warranty and are rated for 150 mph winds!</p>

    <svg class="badge" viewBox="0 0 160 160" aria-hidden="true">
      <circle cx="80" cy="80" r="70" fill="#6ab245"/>
      <circle cx="80" cy="80" r="72" fill="none" stroke="#6ab245" stroke-width="10" stroke-dasharray="5 4"/>
    </svg>
    <p class="badge-text">Available with<br>or without solar<br>and comes in a<br>variety of colors</p>

    <div class="contact-bar"></div>
    <div class="contacts">
      <span class="contact"><span class="icon-disc"><svg width="10" height="10" viewBox="0 0 24 24"><path fill="#fff" d="M5 2l14 11-6 1 4 8-3 1-4-8-5 4z"/></svg></span>www.briskmeadow.com</span>
      <span class="contact"><span class="icon-disc"><svg width="10" height="10" viewBox="0 0 24 24"><path fill="#fff" d="M2 5h20v14H2zm2 2v1l8 5 8-5V7l-8 5z"/></svg></span>hello@briskmeadow.com</span>
    </div>
  </main>
</body>
</html>
```